An expert for Professional and Technical Evaluation of Painting Work Needs a New Letterhead Design

I own a mid-sized painting company and also work as an expert for professional and technical evaluation of painting work in the area of Zurich.

Please read the project description and the must-have-requirements carefully!

I attached 1 PDF which will help you create a new letterhead design:

THE NEW DESIGN DOESN'T NEED A LOGO! (Because it won't represent a company, it represents only a service)
Updates

Dear designers We had a discussion about the location/placement of the design and came to the conclusion that we only want the design to be in the header area of the A4-paper. We would be glad to receive some revised version of your designs. Thank you and kind regards!

Project Deadline Extended
Reason: Due to the fact that only 20% of the designer have understood the brief and submitted designs that have met the requirements we decided to extend the contest deadline.

Project Deadline Extended
Reason: A great deal of good designs were submitted in the last few days. A big thank you to all the participating designers for your good work. We need a few more days to discuss some changes with certain designers and to decide which design will win.

Target Market(s)

(Insurance) Companies, partly also private clients.

Industry/Entity Type

Painting

Colors

Designer to choose colors to be used in the design.

Requirements
Must have
• All information (text, phone numbers, ...) of the old design ("old_letterhead_design.pdf") has also to be in the new one. Additional to that there are a few changes:
The phone numbers "01 583 61 47" and "01 583 61 37" change to "044 583 61 47" and "044 583 61 37". And please mention also this email address: gutachten@valmorkeller.example .

- The design should only be in the header-area of the A4-paper. An the background color of the A4-paper will be white.

- The design should consist of two designs. One for the first page and a smaller version of the design for the following pages.

- THE NEW DESIGN DOESN'T NEED A LOGO! You can make a design with geometric forms, ...

- The new design should have a juridical look. It should only contain colors like brown, fawn, black, light green, ...... colors which look serious/reliable.
Nice to have
• Geometric Forms, Symbols or other design elements.

- It would also be nice to have some design elements which emphasize the kind of work we are offering.

```html
<!DOCTYPE html>
<html lang="de">
<head>
<meta charset="utf-8">
<title>Valmor Keller – Briefpapier</title>
<link href="https://fonts.googleapis.com/css2?family=Open+Sans:wght@400;700&display=swap" rel="stylesheet">
<style>
  :root {
    --stage: #8f8f8f;
    --paper: #ffffff;
    --brown: #5a3e2b;
    --fawn: #b08a5c;
    --ink: #3a2c22;
  }
  * { margin: 0; padding: 0; box-sizing: border-box; }
  html, body { width: 1200px; height: 640px; overflow: hidden; }
  body {
    background: var(--stage);
    font-family: "Open Sans", Arial, sans-serif;
    color: var(--ink);
    position: relative;
  }
  .sheet {
    position: absolute;
    top: 40px;
    width: 396px;
    height: 560px;
    background: var(--paper);
    overflow: hidden;
  }
  .sheet--first { left: 120px; }
  .sheet--follow { left: 684px; }
  .header-swoosh { position: absolute; top: 0; left: 0; display: block; }
  .brand {
    position: absolute;
    display: flex;
    flex-direction: column;
    align-items: center;
    gap: 5px;
    font-weight: 700;
    color: var(--brown);
    white-space: nowrap;
    line-height: 1;
  }
  .brand__mark { background: var(--brown); display: block; }
  .sheet--first .brand { top: 30px; right: 26px; font-size: 14px; }
  .sheet--first .brand__mark { width: 40px; height: 40px; }
  .sheet--follow .brand { top: 24px; right: 22px; font-size: 9px; }
  .sheet--follow .brand__mark { width: 26px; height: 26px; }
  .footer {
    position: absolute;
    left: 0; right: 0; bottom: 14px;
    text-align: center;
    font-size: 6.5px;
    line-height: 1.5;
  }
  .contact-line { display: flex; justify-content: center; align-items: center; gap: 7px; }
  .contact-item { display: inline-flex; align-items: center; gap: 3px; }
  .contact-item svg { width: 8px; height: 8px; display: block; }
  .services { margin-top: 2px; }
</style>
</head>
<body>

<section class="sheet sheet--first" aria-label="Briefpapier erste Seite">
  <svg class="header-swoosh" width="396" height="90" viewBox="0 0 396 90" aria-hidden="true">
    <path d="M0 0 H396 V10 C250 14 110 26 0 50 Z" fill="var(--brown)"/>
    <path d="M0 64 C70 40 170 26 290 22 C180 30 80 46 0 72 Z" fill="var(--fawn)"/>
  </svg>
  <div class="brand"><span class="brand__mark"></span>Valmor Keller</div>

  <footer class="footer">
    <div class="contact-line">
      <span class="contact-item">
        <svg viewBox="0 0 10 10"><circle cx="5" cy="5" r="5" fill="var(--brown)"/><path d="M3 2.6 L4.2 2.4 L4.6 3.8 L4 4.3 C4.4 5.2 4.9 5.7 5.7 6 L6.2 5.4 L7.6 5.8 L7.4 7 C5 7.2 2.8 5 3 2.6 Z" fill="#fff"/></svg>
        044 583 61 47
      </span>
      <span class="contact-item">
        <svg viewBox="0 0 10 10"><circle cx="5" cy="5" r="5" fill="var(--brown)"/><rect x="2.6" y="3" width="4.8" height="4" fill="#fff"/><rect x="3.4" y="3.8" width="3.2" height="1.2" fill="var(--brown)"/></svg>
        044 583 61 37
      </span>
      <span class="contact-item">
        <svg viewBox="0 0 10 10"><circle cx="5" cy="5" r="5" fill="var(--brown)"/><rect x="2.5" y="3.2" width="5" height="3.6" fill="#fff"/><path d="M2.5 3.2 L5 5.2 L7.5 3.2" stroke="var(--brown)" stroke-width="0.6" fill="none"/></svg>
        gutachten@valmorkeller.example
      </span>
      <span class="contact-item">
        <svg viewBox="0 0 10 10"><circle cx="5" cy="5" r="5" fill="var(--brown)"/></svg>
        eidg. dipl. Malermeister
      </span>
    </div>
    <div class="services">Gutachten | Expertisen | Devisierungen | Farbberatungen | Dekorative | Gestaltungen</div>
  </footer>
</section>

<section class="sheet sheet--follow" aria-label="Briefpapier Folgeseite">
  <svg class="header-swoosh" width="396" height="70" viewBox="0 0 396 70" aria-hidden="true">
    <path d="M0 0 H396 V6 C260 10 120 18 0 36 Z" fill="var(--brown)"/>
    <path d="M0 46 C70 28 160 18 250 16 C160 22 80 34 0 52 Z" fill="var(--fawn)"/>
  </svg>
  <div class="brand"><span class="brand__mark"></span>Valmor Keller</div>
</section>

</body>
</html>
```